ARC COURTS Business Card Project

I'd like to request a business card design for the new company I've launched.
The name of the company is "ARC COURTS" an indoor unmanned tennis practice facility.
We would like to see designs that use our brand identity color in the logo I've attached.
We hope to get the design with modern, luxurious and elegant tone and manner.
We hope the logo should not be too big.

Business card must have elements as below:
- Logo (One of the logos I've attached)
- Name (In Korean Text) : 정 우 림
- Title (In Korean Text) : 대표
- Phone Number : 010-5830-2947
- Email Address : woorim.jung@arccourts-example.co.kr
- Website : www.arccourts-example.co.kr
- Instagram : arccourts
- Address (In Korean text) : 경기도 용인시 수지구 풍덕천로 456 미래타워 5층 501호, 502호

Target Market(s)

Tennis amateurs in 20 to 40s

Industry/Entity Type

Sports, Hobby

Contact Information for Business Card

- Logo (One of the logos I've attached) - Name (In Korean Text) : 정 우 림 - Title (In Korean Text) : 대표 - Phone Number : 010-5830-2947 - Email Address : woorim.jung@arccourts-example.co.kr - Website : www.arccourts-example.co.kr - Instagram : arccourts - Address (In Korean text) : 경기도 용인시 수지구 풍덕천로 456 미래타워 5층 501호, 502호

Font styles to use
Sans Serif

Requirements
Must have
• Double sided
Nice to have
• Logo with intaglio or relief embossing
Should not have
• Logo should not be too big.

```html
<!DOCTYPE html>
<html lang="ko">
<head>
<meta charset="UTF-8">
<title>ARC COURTS Business Card</title>
<link href="https://fonts.googleapis.com/css2?family=Noto+Sans+KR:wght@400;500;700&display=swap" rel="stylesheet">
<style>
  :root {
    --brand-green: #2f533a;
    --brand-green-deep: #23402c;
    --ink: #3a3a3a;
    --ink-soft: #666666;
    --rule: #4a4a4a;
    --paper: #ffffff;
    --backdrop: #dcdfe2;
  }
  html, body {
    margin: 0;
    width: 1200px;
    height: 800px;
    overflow: hidden;
    background: var(--backdrop);
    font-family: "Noto Sans KR", sans-serif;
  }
  .canvas {
    width: 1200px;
    height: 800px;
    display: flex;
    align-items: center;
    justify-content: center;
    gap: 40px;
  }
  .card {
    width: 540px;
    height: 310px;
    position: relative;
    box-sizing: border-box;
  }
  .card--back {
    background: var(--paper);
    padding: 30px 36px;
    color: var(--ink);
  }
  .card--front {
    background: var(--brand-green);
    display: flex;
    align-items: center;
    justify-content: center;
  }
  .brand {
    display: flex;
    align-items: center;
    gap: 10px;
  }
  .brand__dot {
    width: 26px;
    height: 26px;
    border-radius: 50%;
    background: var(--brand-green);
  }
  .brand__name {
    font-weight: 500;
    font-size: 22px;
    letter-spacing: 2px;
    color: var(--brand-green);
  }
  .card--front .brand__dot { width: 44px; height: 44px; background: var(--brand-green-deep); }
  .card--front .brand__name { font-size: 34px; letter-spacing: 4px; color: var(--brand-green-deep); }
  .person { margin-top: 30px; }
  .person__name {
    font-weight: 700;
    font-size: 22px;
    color: var(--brand-green);
    letter-spacing: 2px;
    line-height: 1.1;
  }
  .person__title {
    font-size: 15px;
    color: var(--ink-soft);
    margin-top: 2px;
  }
  .contacts {
    margin-top: 18px;
    display: grid;
    grid-template-columns: 200px 1fr;
    font-size: 14px;
    border-bottom: 1px solid var(--rule);
    padding-bottom: 6px;
  }
  .contacts__col--right { padding-top: 20px; }
  .contact {
    display: flex;
    align-items: center;
    gap: 6px;
    line-height: 20px;
    white-space: nowrap;
  }
  .contact svg { width: 12px; height: 12px; flex: none; }
  .address {
    font-size: 14px;
    padding: 8px 0 6px;
    border-bottom: 1px solid var(--rule);
    white-space: nowrap;
  }
</style>
</head>
<body>
<main class="canvas">
  <section class="card card--back">
    <div class="brand">
      <span class="brand__dot"></span>
      <span class="brand__name">ARC COURTS</span>
    </div>
    <div class="person">
      <div class="person__name">정 우 림</div>
      <div class="person__title">대표</div>
    </div>
    <div class="contacts">
      <div class="contacts__col">
        <div class="contact">
          <svg viewBox="0 0 12 12"><path d="M3 1 L5 3.5 L4 4.8 Q5.3 7 7.2 8 L8.5 7 L11 9 L9.8 11 Q5 10.5 1 3 Z" fill="none" stroke="#2f533a" stroke-width="1.2" stroke-linejoin="round"/></svg>
          <span>010-5830-2947</span>
        </div>
        <div class="contact">
          <svg viewBox="0 0 12 12"><rect x="1" y="1" width="10" height="10" fill="none" stroke="#2f533a" stroke-width="1.4"/></svg>
          <span>@arccourts</span>
        </div>
      </div>
      <div class="contacts__col contacts__col--right">
        <div class="contact">
          <svg viewBox="0 0 12 12"><rect x="0.8" y="2" width="10.4" height="8" fill="none" stroke="#2f533a" stroke-width="1.2"/><path d="M1 2.5 L6 6.5 L11 2.5" fill="none" stroke="#2f533a" stroke-width="1.2"/></svg>
          <span>woorim.jung@arccourts-example.co.kr</span>
        </div>
        <div class="contact">
          <svg viewBox="0 0 12 12"><circle cx="6" cy="6" r="5" fill="none" stroke="#2f533a" stroke-width="1.1"/><ellipse cx="6" cy="6" rx="2.2" ry="5" fill="none" stroke="#2f533a" stroke-width="1"/><path d="M1 6 H11" stroke="#2f533a" stroke-width="1"/></svg>
          <span>www.arccourts-example.co.kr</span>
        </div>
      </div>
    </div>
    <div class="address">경기도 용인시 수지구 풍덕천로 456 미래타워 5층 501호, 502호</div>
  </section>

  <section class="card card--front">
    <div class="brand">
      <span class="brand__dot"></span>
      <span class="brand__name">ARC COURTS</span>
    </div>
  </section>
</main>
</body>
</html>
```